Business Card and Stationary Design

After the successful redesign of our logo we are wanting to follow suite and create a new business card and stationary design!

New Logo is attached, information required on the business card should contain a mixture of the following but layout/arrangement is up to the designer.

Happy if the national provider number and abn are on the back, and happy for them to be smaller than the rest.

I am also happy to receive single sided or weird and wonderful designs.

Name
Title
National Provider Number 7291
ABN 53 219 864 317
Level 3, 42 Marlow Street
Ashbury Vale NSW 2291
Ph: 1300 987 214
Mobile: 0432 785 619
name@ferngatebuild.com.au
www.ferngatebuild.com.au

Target Market(s)

Professionals, Peers, Students, Suppliers...

Industry/Entity Type

Construction

Contact Information for Business Card

Listed in project description

Font styles to use
Other font styles liked:
• Century Gothic

Colors
0455a3
3176b5
ffffff

Requirements
Must have
• Professional Design, same color scheme as our logo
Nice to have
• Something that sets our apart from everyone else would be fantastic, open to size and shape and layout options, as long as they present professionally.
• Open to raised/embossed text, alternative materials, custom sizes, clear material
Should not have
• The color orange

```html
<!DOCTYPE html>
<html lang="en">
<head>
<meta charset="utf-8">
<title>Ferngate Build – Business Card</title>
<link href="https://fonts.googleapis.com/css2?family=Questrial&display=swap" rel="stylesheet">
<style>
  :root {
    --backdrop: #1b1b1b;
    --card-white: #ffffff;
    --card-fade: #ececec;
    --brand-blue: #2b3f8f;
    --brand-blue-deep: #243f8c;
    --brand-blue-light: #2f4a98;
    --text-grey: #7a7a7a;
    --rule: #3a4f96;
  }
  * { margin: 0; padding: 0; box-sizing: border-box; }
  html, body {
    width: 900px; height: 1200px; overflow: hidden;
    background: var(--backdrop);
    font-family: "Questrial", "Century Gothic", sans-serif;
  }
  .stage { position: relative; width: 900px; height: 1200px; }

  .card { position: absolute; left: 82px; width: 739px; height: 431px; }
  .card-front {
    top: 132px;
    background: linear-gradient(180deg, var(--card-white) 0%, var(--card-fade) 100%);
    border-radius: 0 50px 0 50px;
    box-shadow: 0 6px 12px rgba(0,0,0,0.45);
  }
  .card-back {
    top: 632px;
    background: linear-gradient(180deg, var(--brand-blue-light) 0%, var(--brand-blue-deep) 100%);
    border-radius: 50px 0 50px 0;
    box-shadow: 0 6px 12px rgba(0,0,0,0.45);
    overflow: hidden;
  }

  .holder { position: absolute; left: 52px; top: 73px; padding-left: 26px; }
  .holder::before {
    content: ""; position: absolute; left: 0; top: 2px;
    width: 6px; height: 40px; background: var(--brand-blue);
  }
  .holder-name { font-size: 26px; color: var(--brand-blue); line-height: 1; letter-spacing: 0.5px; }
  .holder-title { font-size: 17px; color: var(--text-grey); margin-top: 5px; line-height: 1; }

  .brand-mark {
    position: absolute; right: 53px; top: 60px;
    display: flex; align-items: center; gap: 12px;
  }
  .brand-square { width: 22px; height: 22px; background: var(--brand-blue); }
  .brand-name { font-size: 40px; color: var(--brand-blue); line-height: 1; }

  .divider {
    position: absolute; left: 52px; right: 53px; top: 286px;
    height: 1px; background: var(--rule);
  }

  .contact-list {
    position: absolute; left: 52px; top: 309px; list-style: none;
    font-size: 17px; color: var(--brand-blue);
  }
  .contact-list li { display: flex; align-items: center; height: 23px; }
  .contact-list svg { width: 14px; height: 14px; margin-right: 12px; fill: var(--brand-blue); }

  .company-details {
    position: absolute; right: 53px; top: 309px;
    text-align: right; font-size: 17px; color: var(--brand-blue);
  }
  .company-details p { height: 23px; line-height: 23px; white-space: nowrap; }
  .company-details .label { color: var(--text-grey); }

  .back-brand {
    position: absolute; left: 56px; top: 55px;
    font-size: 48px; color: var(--card-white); line-height: 1;
  }
  .back-field {
    position: absolute; right: 0; top: 0; width: 420px; height: 431px;
    background: linear-gradient(180deg, rgba(255,255,255,0.08), rgba(255,255,255,0.04));
  }
</style>
</head>
<body>
<main class="stage">

  <section class="card card-front" aria-label="Business card front">
    <div class="holder">
      <p class="holder-name">DANIEL REEVE</p>
      <p class="holder-title">MANAGING DIRECTOR</p>
    </div>

    <div class="brand-mark">
      <span class="brand-square"></span>
      <span class="brand-name">ferngate build</span>
    </div>

    <div class="divider"></div>

    <ul class="contact-list">
      <li>
        <svg viewBox="0 0 14 14" aria-hidden="true"><path d="M1 4c0-2 2-3 6-3s6 1 6 3v1h-3V4H4v1H1z M3 6h8l1 6H2z"/></svg>
        1300 987 214
      </li>
      <li>
        <svg viewBox="0 0 14 14" aria-hidden="true"><path d="M3 0h8v14H3z M4.5 1.5v8h5v-8z" fill-rule="evenodd"/></svg>
        0432 785 619
      </li>
      <li>
        <svg viewBox="0 0 14 14" aria-hidden="true"><path d="M0 2h14v10H0z M1.5 3.5 7 8l5.5-4.5v7h-11z" fill-rule="evenodd"/></svg>
        name@ferngatebuild.com.au
      </li>
      <li>
        <svg viewBox="0 0 14 14" aria-hidden="true"><circle cx="7" cy="7" r="6" fill="none" stroke="#2b3f8f" stroke-width="1.3"/><ellipse cx="7" cy="7" rx="2.6" ry="6" fill="none" stroke="#2b3f8f" stroke-width="1.1"/><path d="M1 7h12" stroke="#2b3f8f" stroke-width="1.1"/></svg>
        www.ferngatebuild.com.au
      </li>
    </ul>

    <div class="company-details">
      <p>Level 3, 42 Marlow Street</p>
      <p>Ashbury Vale NSW 2291</p>
      <p><span class="label">National Provider Number</span> 7291</p>
      <p><span class="label">ABN</span> 53 219 864 317</p>
    </div>
  </section>

  <section class="card card-back" aria-label="Business card back">
    <div class="back-field" role="img" aria-label="Faint brand block decoration area"></div>
    <p class="back-brand">ferngate build</p>
  </section>

</main>
</body>
</html>
```